Craft a new attractive & professional PowerPoint presentation based on the material provided

Dear Designer,
We are looking for a fresh revamp of our Corporate Power Point presentation. Please find attached:
- the current ppt file;
- new pdf with Corporate profile;
- our logo.
For more information please consult our Social Media Channels:
LinkedIn: https://www.linkedin.com/company/7419063/admin/
IG: https://www.instagram.com/norvapaint/
YT: https://www.youtube.com/channel/UCqWm4TzRk8LpBnDe2VxHjaf
Deadline: before November 20th 2022.
Please do not hesitate to reach out for any questions.
Best wishes,
NRV Marketing Team
Font styles to use
Other font styles liked:
- Helvetica types
Colors
Designer to choose colors to be used in the design.
Look and feel
Each slider illustrates characteristics of the customer's brand and the style your logo design should communicate.

```html
<!DOCTYPE html>
<html lang="en">
<head>
<meta charset="utf-8">
<title>NRV Corporate Presentation – Slide Overview</title>
<link href="https://fonts.googleapis.com/css2?family=Roboto:wght@300;400;500;700&display=swap" rel="stylesheet">
<style>
:root{
  --red:#e3242b;
  --red-dark:#8f1318;
  --ink:#333338;
  --muted:#9d9da3;
  --panel:#f1f1f3;
  --card:#ffffff;
  --navy:#4b5468;
  --green:#2f9e3f;
  --dark:#1b1b1d;
}
*{box-sizing:border-box}
html,body{margin:0;padding:0}
body{width:1200px;height:1057px;overflow:hidden;background:#fff;font-family:'Roboto',Arial,sans-serif;position:relative;color:var(--ink)}
.slide{position:absolute;width:270px;height:150px;background:var(--panel);overflow:hidden;box-shadow:0 5px 12px rgba(0,0,0,.13)}
.slide *{position:absolute;margin:0}
.mark{left:7px;top:5px;width:8px;height:1.3px;background:var(--red)}
.mark::after{content:"";position:absolute;left:9px;top:0;width:3px;height:1.3px;background:var(--ink)}
.title{left:7px;top:9px;font-size:7.4px;font-weight:500;color:var(--ink);white-space:nowrap}
.title em{font-style:normal;color:var(--red)}
.sub{left:7px;top:20px;font-size:2.6px;color:var(--muted)}
.logo{right:7px;top:5px;width:15px;height:13px;background:var(--red);color:#fff;font-size:5px;font-weight:700;display:grid;place-items:center;border-radius:2px}
.url{left:7px;bottom:6px;font-size:3px;color:var(--muted)}
.url b{position:static;font-weight:400;color:var(--red)}
.page{right:7px;bottom:6px;font-size:3px;color:var(--ink);border-left:.5px solid var(--red);padding-left:3px}
.page i{position:absolute;right:7px;font-style:normal}
.band{left:0;bottom:0;width:270px;height:1.6px;background:linear-gradient(90deg,var(--green) 0 33%,transparent 33% 67%,var(--red) 67%)}
.tiny{font-size:2.5px;line-height:1.55;color:var(--muted)}
.lbl{font-size:3px;font-weight:500;color:var(--ink)}
.c{text-align:center}
.card{background:var(--card);box-shadow:0 2px 6px rgba(0,0,0,.08)}
.photo{border-radius:1px}
.yr{font-size:3.6px;font-weight:500;color:var(--ink);text-align:center}
.dash{width:4px;height:.8px;background:var(--red)}
.dark .title{color:#fff}
.dark .url{color:#bbb}
</style>
</head>
<body>

<!-- 1 Title -->
<section class="slide" style="left:47px;top:57px;background:linear-gradient(135deg,#fafafa,#efeff1)">
  <div style="left:125px;top:54px;width:14px;height:1.4px;background:var(--red)"></div>
  <h1 class="c" style="left:0;top:62px;width:270px;font-size:8.4px;font-weight:500;color:#444">Presentation Tittle Goes Here</h1>
  <p class="c" style="left:0;top:77px;width:270px;font-size:4px;color:#777">Credential Subtittle Presentation</p>
  <p class="c" style="left:0;top:99px;width:270px;font-size:4.6px;font-weight:500;color:#555">Mr. Mark <span style="position:static;color:var(--red)">Ellery</span></p>
  <p style="left:7px;top:138px;font-size:3.2px;font-weight:500;color:#444">November <span style="position:static;color:var(--red)">2022</span></p>
  <p style="right:7px;top:138px;font-size:3.2px;font-weight:500;color:#444">www.<span style="position:static;color:var(--red)">norvapaint</span>.com</p>
</section>

<!-- 2 Title dark -->
<section class="slide dark" style="left:326px;top:57px">
  <div class="photo" role="img" aria-label="Close-up of a red branded company shirt" style="left:0;top:0;width:270px;height:150px;background:linear-gradient(120deg,#2b2b2d 0%,#5a1c20 45%,#8b2328 70%,#2a2a2c 100%)"></div>
  <h1 style="left:22px;top:66px;font-size:10px;font-weight:500;color:#fff">Presentation Tittle</h1>
  <p style="left:22px;top:83px;font-size:4px;color:#eee">Your Credential Subtittle Here</p>
  <p style="left:22px;top:101px;font-size:4.2px;color:#fff">Mr. Mark <span style="position:static;color:var(--red)">Ellery</span></p>
</section>

<!-- 3 About Us -->
<section class="slide" style="left:606px;top:57px">
  <div class="mark"></div><h2 class="title">About Us</h2><p class="sub">Here Our Credential Subtittle</p><div class="logo">NRV</div>
  <div class="photo" role="img" aria-label="Hands typing on a laptop keyboard" style="left:26px;top:49px;width:79px;height:66px;background:linear-gradient(135deg,#cfd4da,#6f7782);box-shadow:0 3px 6px rgba(0,0,0,.2)"></div>
  <p class="tiny" style="left:124px;top:50px;width:120px">Lorem ipsum dolor sit amet, consectetuer adipiscing elit. Maecenas porttitor congue massa. Fusce posuere, magna sed pulvinar ultricies, purus lectus malesuada libero, sit amet commodo magna eros quis urna.</p>
  <p class="tiny" style="left:124px;top:72px;width:120px">Nunc viverra imperdiet enim. Fusce est. Vivamus a tellus.</p>
  <p class="tiny" style="left:124px;top:82px;width:120px">Pellentesque habitant morbi tristique senectus et netus et malesuada fames ac turpis egestas. Proin pharetra nonummy pede. Mauris et orci.</p>
  <p class="url">www.<b>norvapaint</b>.com</p><p class="page">page 3</p><div class="band"></div>
</section>

<!-- 4 Family company -->
<section class="slide" style="left:885px;top:57px">
  <div class="mark"></div><h2 class="title">A FAMILY COMPANY</h2><div class="logo">NRV</div>
  <div class="photo" role="img" aria-label="Group photo of the company team in front of the factory" style="left:0;top:28px;width:270px;height:86px;background:linear-gradient(180deg,#a9b9c9 0%,#b89c84 45%,#4b4d52 70%,#5b5e56 100%)"></div>
  <div style="left:65px;top:113px;width:139px;height:15px;background:var(--red)"></div>
  <p class="c" style="left:65px;top:115px;width:139px;font-size:3.5px;line-height:1.55;color:#fff">Driving excellence and keeping on developing innovative products<br>thanks to our incredible <b style="position:static">Team of Talents</b>.</p>
  <p class="url">www.<b>norvapaint</b>.com</p><p class="page">page 4</p><div class="band"></div>
</section>

<!-- 5 Three cards -->
<section class="slide" style="left:47px;top:217px;background:#fafafa">
  <div style="left:131px;top:14px;width:8px;height:.7px;background:#333"></div>
  <h2 class="c" style="left:0;top:17px;width:270px;font-size:7px;font-weight:400;color:#333">Your Tittle <span style="position:static;color:var(--red);font-weight:500">Goes This Slide</span></h2>
  <div class="card" style="left:20px;top:37px;width:62px;height:93px;border-radius:5px"></div>
  <div class="card" style="left:104px;top:37px;width:62px;height:93px;border-radius:5px"></div>
  <div class="card" style="left:188px;top:37px;width:62px;height:93px;border-radius:5px"></div>
  <p class="lbl c" style="left:20px;top:45px;width:62px;font-size:3.3px">Lorem Ipsum One</p>
  <p class="lbl c" style="left:104px;top:45px;width:62px;font-size:3.3px">Lorem Ipsum Two</p>
  <p class="lbl c" style="left:188px;top:44px;width:62px;font-size:3.3px">Lorem Ipsum Three</p>
  <svg style="left:40px;top:62px" width="22" height="18" viewBox="0 0 22 18"><circle cx="6" cy="6" r="5.5" fill="#e3242b"/><path d="M8 12l4-5 3 4m-1 2l4-5 3 5" fill="none" stroke="#e3242b" stroke-width=".5"/></svg>
  <svg style="left:124px;top:62px" width="22" height="18" viewBox="0 0 22 18"><circle cx="6" cy="6" r="5.5" fill="#e3242b"/><path d="M13 3l7 13H6z M13 8v4 M13 13.5v.8" fill="none" stroke="#333" stroke-width=".5"/></svg>
  <svg style="left:208px;top:62px" width="22" height="18" viewBox="0 0 22 18"><circle cx="6" cy="6" r="5.5" fill="#e3242b"/><path d="M12 5l4 4-4 4M8 12l4 4 8-8" fill="none" stroke="#e3242b" stroke-width=".5"/></svg>
  <p class="tiny" style="left:25px;top:87px;width:52px">• Lorem ipsum dolor sit amet, kome consectetuer adipiscing elitan<br>• Lorem ipsum dolor sit amet, kome consectetuer adipiscing elitan<br>• Lorem ipsum dolor sit amet, kome consectetuer adipiscing elitan</p>
  <p class="tiny" style="left:109px;top:87px;width:52px">• Lorem ipsum dolor sit amet, kome consectetuer adipiscing elitan<br>• Lorem ipsum dolor sit amet, kome consectetuer adipiscing elitan<br>• Lorem ipsum dolor sit amet, kome consectetuer adipiscing elitan</p>
  <p class="tiny" style="left:193px;top:87px;width:52px">• Lorem ipsum dolor sit amet, kome consectetuer adipiscing elitan<br>• Lorem ipsum dolor sit amet, kome consectetuer adipiscing elitan<br>• Lorem ipsum dolor sit amet, kome consectetuer adipiscing elitan</p>
  <p style="left:7px;bottom:6px;font-size:3.2px;font-weight:500;color:#333">www.<span style="position:static;color:var(--red)">website</span>.com</p><p class="page">page 5</p>
  <div style="left:0;bottom:0;width:270px;height:1.6px;background:linear-gradient(90deg,var(--navy) 50%,var(--red) 50%)"></div>
</section>

<!-- 6 Six point -->
<section class="slide" style="left:326px;top:217px">
  <div class="mark"></div><h2 class="title">Six Point <em>Company Focus</em></h2><div class="logo">NRV</div>
  <div style="left:101px;top:34px;width:68px;height:42px;background:#fff;border:.5px solid #e7a4a6;box-shadow:0 2px 5px rgba(0,0,0,.1)"></div>
  <svg style="left:0;top:0" width="270" height="150" viewBox="0 0 270 150" fill="none" stroke="#e3242b" stroke-width=".5">
    <rect x="50" y="40" width="10" height="9"/><path d="M52 42l3 5 3-5z"/>
    <path d="M130 48q5-6 10 0M135 40v8m-3-5l3 3 3-3"/>
    <rect x="211" y="40" width="10" height="9"/><path d="M213 47v-3m2.5 3v-5m2.5 5v-2"/>
    <path d="M51 91h8l-1 9h-6zM53 88h4"/>
    <rect x="130" y="90" width="10" height="8" rx="1"/><path d="M132 92v4m2-4v4m2-4v4m2-4v4"/>
    <path d="M216 88l5 9h-10z"/>
    <g stroke-width=".8"><path d="M53 53h4M133 53h4M214 53h4M53 103h4M133 103h4M214 103h4"/></g>
  </svg>
  <p class="lbl c" style="left:25px;top:56px;width:60px;font-size:2.7px">Lorem Ipsum Dolor Sit Amet</p>
  <p class="lbl c" style="left:105px;top:56px;width:60px;font-size:2.7px">Lorem Ipsum Dolor Sit Amet</p>
  <p class="lbl c" style="left:186px;top:56px;width:60px;font-size:2.7px">Lorem Ipsum Dolor Sit Amet</p>
  <p class="tiny c" style="left:25px;top:60px;width:60px">Lorem ipsum dolor sit amet, kome consectetuer adipiscing elitan</p>
  <p class="tiny c" style="left:105px;top:60px;width:60px">Lorem ipsum dolor sit amet, kome consectetuer adipiscing elitan</p>
  <p class="tiny c" style="left:186px;top:60px;width:60px">Lorem ipsum dolor sit amet, kome consectetuer adipiscing elitan</p>
  <p class="lbl c" style="left:25px;top:106px;width:60px;font-size:2.7px">Lorem Ipsum Dolor Sit Amet</p>
  <p class="lbl c" style="left:105px;top:106px;width:60px;font-size:2.7px">Lorem Ipsum Dolor Sit Amet</p>
  <p class="lbl c" style="left:186px;top:106px;width:60px;font-size:2.7px">Lorem Ipsum Dolor Sit Amet</p>
  <p class="tiny c" style="left:25px;top:110px;width:60px">Lorem ipsum dolor sit amet, kome consectetuer adipiscing elitan</p>
  <p class="tiny c" style="left:105px;top:110px;width:60px">Lorem ipsum dolor sit amet, kome consectetuer adipiscing elitan</p>
  <p class="tiny c" style="left:186px;top:110px;width:60px">Lorem ipsum dolor sit amet, kome consectetuer adipiscing elitan</p>
  <p class="url">www.<b>norvapaint</b>.com</p><p class="page">page 6</p><div class="band"></div>
</section>

<!-- 7 Six cards -->
<section class="slide" style="left:606px;top:217px">
  <div class="mark"></div><h2 class="title">Your Tittle <em>This Slide</em></h2><div class="logo">NRV</div>
  <div style="left:14px;top:32px;width:74px;height:44px;background:var(--red)"></div>
  <div class="card" style="left:97px;top:32px;width:74px;height:44px"></div>
  <div class="card" style="left:181px;top:32px;width:74px;height:44px"></div>
  <div class="card" style="left:14px;top:86px;width:74px;height:44px"></div>
  <div class="card" style="left:97px;top:86px;width:74px;height:44px"></div>
  <div class="card" style="left:181px;top:86px;width:74px;height:44px"></div>
  <p class="lbl" style="left:19px;top:49px;color:#fff;font-size:3px">Lorem Ipsum Dolor Sit Amet</p>
  <p class="tiny" style="left:19px;top:55px;width:60px;color:#fbdcdd">Lorem ipsum dolor sit amet, kome consectetuer adipiscing elitan</p>
  <p class="lbl" style="left:102px;top:49px;font-size:3px">Lorem Ipsum Dolor Sit Amet</p>
  <p class="tiny" style="left:102px;top:55px;width:60px">Lorem ipsum dolor sit amet, kome consectetuer adipiscing elitan</p>
  <p class="lbl" style="left:186px;top:49px;font-size:3px">Lorem Ipsum Dolor Sit Amet</p>
  <p class="tiny" style="left:186px;top:55px;width:60px">Lorem ipsum dolor sit amet, kome consectetuer adipiscing elitan</p>
  <p class="lbl" style="left:19px;top:103px;font-size:3px">Lorem Ipsum Dolor Sit Amet</p>
  <p class="tiny" style="left:19px;top:109px;width:60px">Lorem ipsum dolor sit amet, kome consectetuer adipiscing elitan</p>
  <p class="lbl" style="left:102px;top:103px;font-size:3px">Lorem Ipsum Dolor Sit Amet</p>
  <p class="tiny" style="left:102px;top:109px;width:60px">Lorem ipsum dolor sit amet, kome consectetuer adipiscing elitan</p>
  <p class="lbl" style="left:186px;top:103px;font-size:3px">Lorem Ipsum Dolor Sit Amet</p>
  <p class="tiny" style="left:186px;top:109px;width:60px">Lorem ipsum dolor sit amet, kome consectetuer adipiscing elitan</p>
  <svg style="left:0;top:0" width="270" height="150" viewBox="0 0 270 150" fill="none" stroke-width=".5">
    <path d="M80 37l2 3h-4z" stroke="#fff"/><path d="M162 36l4 6h-8z" stroke="#e3242b"/><rect x="245" y="36" width="6" height="5" stroke="#e3242b"/>
    <path d="M77 93l4-3" stroke="#e3242b"/><rect x="162" y="89" width="5" height="7" stroke="#e3242b"/><path d="M244 94q3-4 6 0" stroke="#e3242b"/>
    <g stroke="#e3242b" stroke-width=".7"><path d="M19 53h3M102 53h3M186 53h3M19 107h3M102 107h3M186 107h3"/></g>
  </svg>
  <p class="url">www.<b>norvapaint</b>.com</p><p class="page">page 7</p><div class="band"></div>
</section>

<!-- 8 Circle chart -->
<section class="slide" style="left:885px;top:217px">
  <div class="mark"></div><h2 class="title">Circle Chart <em>Analyse</em></h2><div class="logo">NRV</div>
  <div class="card" style="left:18px;top:36px;width:93px;height:85px"></div>
  <div class="card" style="left:120px;top:36px;width:133px;height:85px"></div>
  <p class="lbl" style="left:24px;top:42px;font-size:3.4px">Circle Finding Chart</p>
  <svg style="left:18px;top:36px" width="93" height="85" viewBox="0 0 93 85" fill="none">
    <circle cx="47" cy="47" r="27" stroke="#4b5468" stroke-width=".7"/>
    <circle cx="47" cy="47" r="23" stroke="#e3242b" stroke-width=".7" stroke-dasharray="110 40"/>
    <circle cx="47" cy="47" r="19" stroke="#e3242b" stroke-width=".7" stroke-dasharray="90 40"/>
    <circle cx="58" cy="28" r="3.5" fill="#4b5468"/><text x="58" y="29.2" font-size="3.4" fill="#fff" text-anchor="middle">1</text>
    <circle cx="62" cy="64" r="3.5" fill="#e3242b"/><text x="62" y="65.2" font-size="3.4" fill="#fff" text-anchor="middle">2</text>
    <circle cx="18" cy="50" r="3.5" fill="#4b5468"/><text x="18" y="51.2" font-size="3.4" fill="#fff" text-anchor="middle">3</text>
  </svg>
  <p class="tiny" style="left:127px;top:44px;width:120px"><b style="position:static;color:#333">◦ Analyse Two:</b><br>Lorem ipsum dolor sit amet, consectetuer adipiscing elit. Maecenas porttitor congue massa. Fusce posuere, magna sed pulvinar ultricies, purus lectus malesuada.</p>
  <p class="tiny" style="left:127px;top:68px;width:120px"><b style="position:static;color:#333">◦ Analyse Two:</b><br>Lorem ipsum dolor sit amet, consectetuer adipiscing elit. Maecenas porttitor congue massa. Fusce posuere, magna sed pulvinar ultricies, purus lectus malesuada.</p>
  <p class="tiny" style="left:127px;top:92px;width:120px"><b style="position:static;color:#333">◦ Analyse Two:</b><br>Lorem ipsum dolor sit amet, consectetuer adipiscing elit. Maecenas porttitor congue massa. Fusce posuere, magna sed pulvinar ultricies, purus lectus malesuada.</p>
  <p class="url">www.<b>norvapaint</b>.com</p><p class="page">page 8</p><div class="band"></div>
</section>

<!-- 9 Bar chart -->
<section class="slide" style="left:47px;top:377px">
  <div class="mark"></div><h2 class="title" style="left:10px">Bar Chart <em>Analyse</em></h2><div class="logo">NRV</div>
  <div class="card" style="left:18px;top:36px;width:93px;height:85px"></div>
  <div class="card" style="left:120px;top:36px;width:133px;height:85px"></div>
  <p class="lbl" style="left:24px;top:42px;font-size:3.4px">Circle Finding Chart</p>
  <svg style="left:18px;top:36px" width="93" height="85" viewBox="0 0 93 85">
    <g font-size="2.6" fill="#555" text-anchor="end"><text x="30" y="24">Data Five</text><text x="30" y="35">Data Four</text><text x="30" y="46">Data Three</text><text x="30" y="57">Data Two</text><text x="30" y="68">Data One</text></g>
    <rect x="32" y="21.5" width="12" height="3.2" fill="#e3242b"/>
    <rect x="32" y="32.5" width="16" height="3.2" fill="#9aa83a"/>
    <rect x="32" y="43.5" width="27" height="3.2" fill="#4b5468"/>
    <rect x="32" y="54.5" width="32" height="3.2" fill="#f26a2f"/>
    <rect x="32" y="65.5" width="36" height="3.2" fill="#8c94a6"/>
    <g font-size="2.6" fill="#555" text-anchor="middle"><text x="35" y="77">0</text><text x="53" y="77">100</text><text x="72" y="77">200</text></g>
  </svg>
  <p class="tiny" style="left:127px;top:44px;width:120px"><b style="position:static;color:#333">◦ Analyse Two:</b><br>Lorem ipsum dolor sit amet, consectetuer adipiscing elit. Maecenas porttitor congue massa. Fusce posuere, magna sed pulvinar ultricies, purus lectus malesuada.</p>
  <p class="tiny" style="left:127px;top:68px;width:120px"><b style="position:static;color:#333">◦ Analyse Two:</b><br>Lorem ipsum dolor sit amet, consectetuer adipiscing elit. Maecenas porttitor congue massa. Fusce posuere, magna sed pulvinar ultricies, purus lectus malesuada.</p>
  <p class="tiny" style="left:127px;top:92px;width:120px"><b style="position:static;color:#333">◦ Analyse Two:</b><br>Lorem ipsum dolor sit amet, consectetuer adipiscing elit. Maecenas porttitor congue massa. Fusce posuere, magna sed pulvinar ultricies, purus lectus malesuada.</p>
  <p class="url">www.<b>norvapaint</b>.com</p><p class="page">page 9</p><div class="band"></div>
</section>

<!-- 10 Awards -->
<section class="slide" style="left:326px;top:377px">
  <div class="mark"></div><h2 class="title">Our Awards</h2><p class="sub">Company Profile</p><div class="logo">NRV</div>
  <div class="photo" role="img" aria-label="Glass award plaque on dark background" style="left:19px;top:44px;width:62px;height:38px;background:linear-gradient(135deg,#3a3d40,#121314)"></div>
  <div class="photo" role="img" aria-label="Golden trophy cup" style="left:104px;top:44px;width:62px;height:38px;background:linear-gradient(135deg,#e4e4e2,#a9a7a0)"></div>
  <div class="photo" role="img" aria-label="Hand holding a small award" style="left:189px;top:44px;width:62px;height:38px;background:linear-gradient(135deg,#2a2a2a,#6b4636 60%,#151515)"></div>
  <p class="yr" style="left:19px;top:93px;width:62px">2019</p><p class="yr" style="left:104px;top:93px;width:62px">2020</p><p class="yr" style="left:189px;top:92px;width:62px">2021</p>
  <div class="dash" style="left:48px;top:99px"></div><div class="dash" style="left:133px;top:99px"></div><div class="dash" style="left:218px;top:98px"></div>
  <p class="tiny c" style="left:17px;top:103px;width:66px">Lorem ipsum dolor sit amet, consectetuer adipisc. Maecenas porttitor congue massa kame.</p>
  <p class="tiny c" style="left:102px;top:103px;width:66px">Lorem ipsum dolor sit amet, consectetuer adipisc. Maecenas porttitor congue massa kame.</p>
  <p class="tiny c" style="left:187px;top:102px;width:66px">Lorem ipsum dolor sit amet, consectetuer adipisc. Maecenas porttitor congue massa kame.</p>
  <p class="url">www.<b>norvapaint</b>.com</p><p class="page">page 10</p><div class="band"></div>
</section>

<!-- 11 Picture drop -->
<section class="slide" style="left:606px;top:377px">
  <div class="mark"></div><h2 class="title">Picture Drop Here</h2><div class="logo">NRV</div>
  <div class="photo" role="img" aria-label="Hands holding industrial abrasive brushes" style="left:15px;top:39px;width:53px;height:64px;background:linear-gradient(135deg,#8a7768,#3f4a55 60%,#6d6258)"></div>
  <div class="photo" role="img" aria-label="Visitors at a research facility exhibition" style="left:77px;top:39px;width:53px;height:64px;background:linear-gradient(180deg,#7f97ad,#3a3a40 60%,#2b2b2e)"></div>
  <div class="photo" role="img" aria-label="Red branded company shirt close-up" style="left:139px;top:39px;width:53px;height:64px;background:linear-gradient(135deg,#c2202a,#8f1a20 60%,#d8454b)"></div>
  <div class="photo" role="img" aria-label="Company building under a cloudy sky" style="left:201px;top:39px;width:53px;height:64px;background:linear-gradient(180deg,#b4c4d3,#d9dfe4 50%,#9a8c7b 75%,#6f6c66)"></div>
  <div class="dash" style="left:40px;top:107px"></div><div class="dash" style="left:102px;top:107px"></div><div class="dash" style="left:164px;top:107px"></div><div class="dash" style="left:226px;top:107px"></div>
  <p class="tiny c" style="left:13px;top:111px;width:57px">Lorem ipsum dolor sit amet, consectetuer adipisc. Maecenas porttitor congue massa kame.</p>
  <p class="tiny c" style="left:75px;top:111px;width:57px">Lorem ipsum dolor sit amet, consectetuer adipisc. Maecenas porttitor congue massa kame.</p>
  <p class="tiny c" style="left:137px;top:111px;width:57px">Lorem ipsum dolor sit amet, consectetuer adipisc. Maecenas porttitor congue massa kame.</p>
  <p class="tiny c" style="left:199px;top:111px;width:57px">Lorem ipsum dolor sit amet, consectetuer adipisc. Maecenas porttitor congue massa kame.</p>
  <p class="url">www.<b>norvapaint</b>.com</p><p class="page">page 11</p><div class="band"></div>
</section>

<!-- 12 Awards -->
<section class="slide" style="left:885px;top:377px">
  <div class="mark"></div><h2 class="title" style="top:11px">Our Awards</h2><p class="sub" style="top:22px">Here Our Credential Subtittle</p><div class="logo">NRV</div>
  <div class="photo" role="img" aria-label="Glass award plaque on dark background" style="left:19px;top:44px;width:62px;height:38px;background:linear-gradient(135deg,#3a3d40,#121314)"></div>
  <div class="photo" role="img" aria-label="Golden trophy cup" style="left:104px;top:44px;width:62px;height:38px;background:linear-gradient(135deg,#e4e4e2,#a9a7a0)"></div>
  <div class="photo" role="img" aria-label="Hand holding a small award" style="left:189px;top:44px;width:62px;height:38px;background:linear-gradient(135deg,#2a2a2a,#6b4636 60%,#151515)"></div>
  <p class="yr" style="left:19px;top:93px;width:62px">2019</p><p class="yr" style="left:104px;top:93px;width:62px">2020</p><p class="yr" style="left:189px;top:92px;width:62px">2021</p>
  <div class="dash" style="left:48px;top:99px"></div><div class="dash" style="left:133px;top:99px"></div><div class="dash" style="left:218px;top:98px"></div>
  <p class="tiny c" style="left:17px;top:103px;width:66px">Lorem ipsum dolor sit amet, consectetuer adipisc. Maecenas porttitor congue massa kame.</p>
  <p class="tiny c" style="left:102px;top:103px;width:66px">Lorem ipsum dolor sit amet, consectetuer adipisc. Maecenas porttitor congue massa kame.</p>
  <p class="tiny c" style="left:187px;top:102px;width:66px">Lorem ipsum dolor sit amet, consectetuer adipisc. Maecenas porttitor congue massa kame.</p>
  <p class="url">www.<b>norvapaint</b>.com</p><p class="page">page 12</p><div class="band"></div>
</section>

<!-- 13 Content page -->
<section class="slide" style="left:47px;top:537px">
  <div class="mark"></div><h2 class="title" style="top:11px">Content Page with Tittle</h2><p class="sub" style="top:22px">Here Our Credential Subtittle</p><div class="logo">NRV</div>
  <div class="photo" role="img" aria-label="Laptop and plant on a desk" style="left:19px;top:40px;width:55px;height:65px;background:linear-gradient(135deg,#e9ebec,#9fa6a8 60%,#3c4a36)"></div>
  <div class="photo" role="img" aria-label="Business people in a meeting outdoors" style="left:77px;top:66px;width:55px;height:65px;background:linear-gradient(135deg,#7d9b5d,#2d3442 60%,#1d2430);box-shadow:-2px 0 0 #f1f1f3"></div>
  <p style="left:141px;top:45px;width:112px;font-size:4.2px;line-height:1.5;color:#777"><span style="position:static;color:var(--red);font-weight:500">Lorem ipsum</span> dolor sit amet consectetuer adipiscing elit maecenas porttitor</p>
  <p class="tiny" style="left:141px;top:62px;width:112px"><b style="position:static;color:#333">Lorem ipsum</b> dolor sit amet, consectetuer adipiscing elit. Maecenas porttitor congue massa. Fusce posuere, magna sed pulvinar ultricies, purus lectus malesuada libero, sit amet commodo magna eros quis urna. Nunc viverra imperdiet enim. Fusce est. Vivamus a tellus. Pellentesque habitant morbi tristique senectus et netus et malesuada fames ac turpis egestas.</p>
  <p class="tiny" style="left:141px;top:93px;width:112px">Lorem ipsum dolor sit amet, consectetuer adipiscing elit. Maecenas porttitor congue massa. Fusce posuere, magna sed pulvinar ultricies, purus lectus malesuada libero, sit amet commodo magna eros quis urna. Nunc viverra imperdiet enim.</p>
  <p class="url">www.<b>norvapaint</b>.com</p><p class="page">page 13</p><div class="band"></div>
</section>

<!-- 14 Content stats -->
<section class="slide" style="left:326px;top:537px">
  <div class="mark"></div><h2 class="title" style="top:11px">Content Page with Tittle</h2><p class="sub" style="top:22px">Here Our Credential Subtittle</p><div class="logo">NRV</div>
  <div style="left:131px;top:46px;width:7px;height:.8px;background:var(--red)"></div>
  <p class="tiny c" style="left:30px;top:52px;width:210px"><b style="position:static;color:var(--red)">Lorem ipsum</b> dolor sit amet, consectetuer adipiscing elit. Maecenas porttitor congue massa. Fusce posuere, magna sed pulvinar ultricies, purus lectus malesuada libero, sit amet commodo magna eros quis urna.Nunc viverra imperdiet enim. Fusce est. Vivamus a tellus. Pellentesque habitant morbi tristique senectus et netus et malesuada fames ac turpis egestas. Proin pharetra nonummy pede. Mauris et orci.</p>
  <p class="c" style="left:20px;top:88px;width:50px;font-size:7px;font-weight:500;color:#333">320</p><p class="tiny c" style="left:20px;top:97px;width:50px;font-size:3px">Customers Served</p>
  <p class="c" style="left:77px;top:88px;width:50px;font-size:7px;font-weight:500;color:#333">1281</p><p class="tiny c" style="left:77px;top:97px;width:50px;font-size:3px">Projects Completed</p>
  <p class="c" style="left:134px;top:88px;width:50px;font-size:7px;font-weight:500;color:#333">8700</p><p class="tiny c" style="left:134px;top:97px;width:50px;font-size:3px">Project Hours</p>
  <p class="c" style="left:191px;top:88px;width:50px;font-size:7px;font-weight:500;color:#333">14</p><p class="tiny c" style="left:191px;top:97px;width:50px;font-size:3px">Certifications</p>
  <p class="url">www.<b>norvapaint</b>.com</p><p class="page">page 14</p><div class="band"></div>
</section>

<!-- 15 Presentation content timeline -->
<section class="slide" style="left:606px;top:537px">
  <div class="mark"></div><h2 class="title" style="top:11px">Presentation Content</h2><p class="sub" style="top:22px">Here Our Credential Subtittle</p><div class="logo">NRV</div>
  <svg style="left:0;top:0" width="270" height="150" viewBox="0 0 270 150">
    <line x1="16" y1="82" x2="254" y2="82" stroke="#bbb" stroke-width=".4"/>
    <circle cx="16" cy="82" r="1" fill="none" stroke="#bbb" stroke-width=".4"/><circle cx="254" cy="82" r="1" fill="none" stroke="#bbb" stroke-width=".4"/>
    <g stroke="#999" stroke-width=".4" stroke-dasharray="1 1"><path d="M77 62v14M153 62v14M229 62v14M39 88v14M115 88v14"/></g>
    <path d="M191 88v14" stroke="#e3242b" stroke-width=".5" stroke-dasharray="1 1"/>
    <g fill="#4b5468" stroke="#d5d7dc" stroke-width="1.2"><circle cx="39" cy="82" r="5"/><circle cx="77" cy="82" r="5"/><circle cx="115" cy="82" r="5"/><circle cx="153" cy="82" r="5"/><circle cx="229" cy="82" r="5"/></g>
    <circle cx="191" cy="82" r="8" fill="#e3242b" stroke="#f6c3c5" stroke-width="1.6"/>
    <g font-size="2.8" fill="#fff" text-anchor="middle" font-weight="500"><text x="39" y="83">2018</text><text x="77" y="83">2019</text><text x="115" y="83">2020</text><text x="153" y="83">2021</text><text x="191" y="83">2022</text><text x="229" y="83">2023</text></g>
    <g fill="none" stroke="#333" stroke-width=".4"><rect x="75" y="39" width="5" height="3.5"/><circle cx="152" cy="40" r="1.7"/><path d="M153 41l2 2"/><rect x="227" y="39" width="5" height="3.5"/><path d="M39 104v4m-2-2h4"/><path d="M115 104l2 4h-4z"/></g>
  </svg>
  <p class="lbl c" style="left:52px;top:46px;width:50px;font-size:2.7px">Lorem Ipsum</p><p class="tiny c" style="left:52px;top:50px;width:50px;font-size:2.2px">Lorem ipsum dolor sit amet, consectetuer adipisc. Maecenas porttitor congue.</p>
  <p class="lbl c" style="left:128px;top:46px;width:50px;font-size:2.7px">Lorem Ipsum</p><p class="tiny c" style="left:128px;top:50px;width:50px;font-size:2.2px">Lorem ipsum dolor sit amet, consectetuer adipisc. Maecenas porttitor congue.</p>
  <p class="lbl c" style="left:204px;top:46px;width:50px;font-size:2.7px">Lorem Ipsum</p><p class="tiny c" style="left:204px;top:50px;width:50px;font-size:2.2px">Lorem ipsum dolor sit amet, consectetuer adipisc. Maecenas porttitor congue.</p>
  <p class="lbl c" style="left:14px;top:111px;width:50px;font-size:2.7px">Lorem Ipsum</p><p class="tiny c" style="left:14px;top:115px;width:50px;font-size:2.2px">Lorem ipsum dolor sit amet, consectetuer adipisc. Maecenas porttitor congue.</p>
  <p class="lbl c" style="left:90px;top:111px;width:50px;font-size:2.7px">Lorem Ipsum</p><p class="tiny c" style="left:90px;top:115px;width:50px;font-size:2.2px">Lorem ipsum dolor sit amet, consectetuer adipisc. Maecenas porttitor congue.</p>
  <p class="lbl c" style="left:166px;top:106px;width:50px;font-size:2.7px;color:var(--red)">The Goal</p><p class="tiny c" style="left:166px;top:111px;width:50px;font-size:2.2px">Lorem ipsum dolor sit amet, consectetuer adipisc. Maecenas porttitor congue.</p>
  <p class="url">www.<b>norvapaint</b>.com</p><p class="page">page 15</p><div class="band"></div>
</section>

<!-- 16 Project timeline -->
<section class="slide" style="left:885px;top:537px">
  <div class="mark"></div><h2 class="title" style="top:11px">Project Timeline</h2><p class="sub" style="top:22px">Here Our Credential Subtittle</p><div class="logo">NRV</div>
  <svg style="left:0;top:0" width="270" height="150" viewBox="0 0 270 150"><line x1="135" y1="34" x2="135" y2="150" stroke="#ccc" stroke-width=".4"/><circle cx="135" cy="34" r="1.4" fill="#4b5468"/><circle cx="135" cy="65" r="1" fill="#e3242b"/><circle cx="135" cy="92" r="1" fill="#e3242b"/><circle cx="135" cy="117" r="1" fill="#e3242b"/></svg>
  <p class="lbl" style="right:139px;top:39px;font-size:2.6px">May 2022</p><p class="tiny" style="right:139px;top:43px;width:55px;text-align:right;font-size:2.2px">Lorem ipsum dolor sit amet, consectetuer adipisc. Maecenas porttitor congue.</p>
  <p class="lbl" style="left:139px;top:66px;font-size:2.6px">June 2022</p><p class="tiny" style="left:139px;top:70px;width:55px;font-size:2.2px">Lorem ipsum dolor sit amet, consectetuer adipisc. Maecenas porttitor congue.</p>
  <p class="lbl" style="right:139px;top:92px;font-size:2.6px">July 2022</p><p class="tiny" style="right:139px;top:96px;width:55px;text-align:right;font-size:2.2px">Lorem ipsum dolor sit amet, consectetuer adipisc. Maecenas porttitor congue.</p>
  <p class="lbl" style="left:139px;top:120px;font-size:2.6px">August 2022</p><p class="tiny" style="left:139px;top:124px;width:55px;font-size:2.2px">Lorem ipsum dolor sit amet, consectetuer adipisc. Maecenas porttitor congue.</p>
  <p class="url">www.<b>norvapaint</b>.com</p><p class="page">page 16</p><div class="band"></div>
</section>

<!-- 17 Timeline continued -->
<section class="slide" style="left:47px;top:697px">
  <div class="mark"></div><div class="logo">NRV</div>
  <svg style="left:0;top:0" width="270" height="150" viewBox="0 0 270 150"><line x1="135" y1="0" x2="135" y2="115" stroke="#ccc" stroke-width=".4"/><circle cx="135" cy="25" r="1" fill="#e3242b"/><circle cx="135" cy="54" r="1" fill="#e3242b"/><circle cx="135" cy="85" r="1" fill="#e3242b"/><circle cx="135" cy="115" r="1.4" fill="#4b5468"/></svg>
  <p class="lbl" style="right:139px;top:27px;font-size:2.6px">September 2022</p><p class="tiny" style="right:139px;top:31px;width:55px;text-align:right;font-size:2.2px">Lorem ipsum dolor sit amet, consectetuer adipisc. Maecenas porttitor congue.</p>
  <p class="lbl" style="left:139px;top:57px;font-size:2.6px">October 2022</p><p class="tiny" style="left:139px;top:61px;width:55px;font-size:2.2px">Lorem ipsum dolor sit amet, consectetuer adipisc. Maecenas porttitor congue.</p>
  <p class="lbl" style="right:139px;top:86px;font-size:2.6px">November 2022</p><p class="tiny" style="right:139px;top:90px;width:55px;text-align:right;font-size:2.2px">Lorem ipsum dolor sit amet, consectetuer adipisc. Maecenas porttitor congue.</p>
  <p class="lbl" style="left:139px;top:116px;font-size:2.6px">December 2022</p><p class="tiny" style="left:139px;top:120px;width:55px;font-size:2.2px">Lorem ipsum dolor sit amet, consectetuer adipisc. Maecenas porttitor congue.</p>
  <p class="url">www.<b>norvapaint</b>.com</p><p class="page">page 17</p><div class="band"></div>
</section>

<!-- 18 Next step -->
<section class="slide" style="left:326px;top:697px">
  <div class="mark"></div><h2 class="title">The Next Step for Closer</h2><div class="logo">NRV</div>
  <svg style="left:0;top:0" width="270" height="150" viewBox="0 0 270 150">
    <defs><linearGradient id="pill" x1="0" y1="0" x2="0" y2="1"><stop offset="0" stop-color="#4b5468"/><stop offset=".5" stop-color="#4b5468"/><stop offset=".5" stop-color="#e3242b"/><stop offset="1" stop-color="#e3242b"/></linearGradient></defs>
    <g fill="url(#pill)"><rect x="36" y="40" width="21" height="40" rx="10.5"/><rect x="95" y="40" width="21" height="40" rx="10.5"/><rect x="154" y="40" width="21" height="40" rx="10.5"/><rect x="213" y="40" width="21" height="40" rx="10.5"/></g>
    <g font-size="3" fill="#fff" text-anchor="middle"><text x="46.5" y="61">One</text><text x="105.5" y="61">Two</text><text x="164.5" y="61">Three</text><text x="223.5" y="61">Four</text></g>
    <g fill="#e3242b"><path d="M46.5 104l6 3.5v7l-6 3.5-6-3.5v-7z"/><path d="M105.5 104l6 3.5v7l-6 3.5-6-3.5v-7z"/><path d="M164.5 104l6 3.5v7l-6 3.5-6-3.5v-7z"/><path d="M223.5 104l6 3.5v7l-6 3.5-6-3.5v-7z"/></g>
    <g fill="none" stroke="#fff" stroke-width=".5"><circle cx="46.5" cy="111" r="2"/><path d="M105.5 108v6m-2 0h4"/><rect x="162.5" y="109" width="4" height="4"/><path d="M221.5 113h4v-3"/></g>
  </svg>
  <p class="tiny c" style="left:22px;top:86px;width:49px">Lorem ipsum dolor sit amet, consectetuer adipiscing elit. Maecen portion congue massa.</p>
  <p class="tiny c" style="left:81px;top:86px;width:49px">Lorem ipsum dolor sit amet, consectetuer adipiscing elit. Maecen portion congue massa.</p>
  <p class="tiny c" style="left:140px;top:86px;width:49px">Lorem ipsum dolor sit amet, consectetuer adipiscing elit. Maecen portion congue massa.</p>
  <p class="tiny c" style="left:199px;top:86px;width:49px">Lorem ipsum dolor sit amet, consectetuer adipiscing elit. Maecen portion congue massa.</p>
  <p class="url">www.<b>norvapaint</b>.com</p><p class="page">page 18</p><div class="band"></div>
</section>

<!-- 19 Table -->
<section class="slide dark" style="left:606px;top:697px;background:linear-gradient(135deg,#141415 30%,#3a1114 70%,#a5161d)">
  <div class="mark" style="background:#fff"></div><h2 class="title">Table Rate Chart</h2><div class="logo" style="background:#777">NRV</div>
  <svg style="left:38px;top:38px" width="196" height="85" viewBox="0 0 196 85" font-size="2.8" text-anchor="middle">
    <rect width="196" height="8" fill="#e3242b"/>
    <g fill="#fff" font-weight="500"><text x="17" y="5">Data Name</text><text x="62" y="5">Number</text><text x="98" y="5">Profit Rate</text><text x="127" y="5">Option</text><text x="151" y="5">Rate</text><text x="177" y="5">Performance</text></g>
    <g fill="#fff" fill-opacity=".1"><rect y="21" width="196" height="12"/><rect y="45" width="196" height="12"/><rect y="69" width="196" height="12"/></g>
    <g fill="#ddd">
      <text x="14" y="16">Data One</text><text x="62" y="16">5,887</text><text x="98" y="16">20.45</text><text x="127" y="16">Yes</text><text x="151" y="16">70</text><text x="177" y="16">3,566</text>
      <text x="14" y="28">Data Two</text><text x="62" y="28">6,5444</text><text x="98" y="28">34.5</text><text x="127" y="28">Yes</text><text x="151" y="28">67</text><text x="177" y="28">3,997</text>
      <text x="15" y="40">Data Three</text><text x="62" y="40">54,333</text><text x="98" y="40">56.7</text><text x="127" y="40">No</text><text x="151" y="40">77</text><text x="177" y="40">9,887</text>
      <text x="14" y="52">Data Four</text><text x="62" y="52">7,655</text><text x="98" y="52">6.55</text><text x="127" y="52">No</text><text x="151" y="52">89</text><text x="177" y="52">97,666</text>
      <text x="14" y="64">Data Five</text><text x="62" y="64">7,665</text><text x="98" y="64">90</text><text x="127" y="64">Yes</text><text x="151" y="64">90</text><text x="177" y="64">88.9</text>
      <text x="13" y="76">Data Six</text><text x="62" y="76">9,999</text><text x="98" y="76">69</text><text x="127" y="76">No.</text><text x="151" y="76">87</text><text x="177" y="76">98.7</text>
    </g>
  </svg>
  <p class="url">www.<b>norvapaint</b>.com</p><p class="page" style="color:#eee">page 19</p>
</section>

<!-- 20 Calendar -->
<section class="slide" style="left:885px;top:697px">
  <div class="mark"></div><h2 class="title">Montly Calendar Planning</h2><div class="logo">NRV</div>
  <div class="card" style="left:31px;top:48px;width:62px;height:72px"></div>
  <div class="card" style="left:105px;top:48px;width:62px;height:72px"></div>
  <div class="card" style="left:179px;top:48px;width:62px;height:72px"></div>
  <svg style="left:0;top:0" width="270" height="150" viewBox="0 0 270 150"><circle cx="62" cy="60" r="3" fill="#e3242b"/><g fill="none" stroke="#e3242b" stroke-width=".5"><path d="M136 57v6m-3-3h6m-2-2l2-2m-6 0l2 2m0 4l-2 2m6 0l-2-2"/><rect x="207" y="57" width="6" height="5"/><path d="M208 61l2-2 2 2"/></g></svg>
  <p class="c" style="left:31px;top:66px;width:62px;font-size:4.2px;font-weight:700;color:var(--red)">23<sup style="position:static;font-size:2.5px">rd</sup></p><p class="tiny c" style="left:31px;top:72px;width:62px">June</p>
  <p class="c" style="left:105px;top:66px;width:62px;font-size:4.2px;font-weight:700;color:var(--red)">11<sup style="position:static;font-size:2.5px">st</sup></p><p class="tiny c" style="left:105px;top:72px;width:62px">July</p>
  <p class="c" style="left:179px;top:66px;width:62px;font-size:4.2px;font-weight:700;color:var(--red)">2<sup style="position:static;font-size:2.5px">nd</sup></p><p class="tiny c" style="left:179px;top:72px;width:62px">August</p>
  <p class="tiny" style="left:36px;top:80px;width:55px">• Identify the lorem ipsum dolor<br>• The dolor lorem with ipsume<br>• Sit amet lorem to the dolor<br>• The lorem ipsume for dolor sit</p>
  <p class="tiny" style="left:110px;top:80px;width:55px">• Identify the lorem ipsum dolor<br>• The dolor lorem with ipsume<br>• Sit amet lorem to the dolor<br>• The lorem ipsume for dolor sit</p>
  <p class="tiny" style="left:184px;top:80px;width:55px">• Identify the lorem ipsum dolor<br>• The dolor lorem with ipsume<br>• Sit amet lorem to the dolor<br>• The lorem ipsume for dolor sit</p>
  <p class="url">www.<b>norvapaint</b>.com</p><p class="page">page 20</p><div class="band"></div>
</section>

<!-- 21 Monthly report -->
<section class="slide" style="left:47px;top:857px">
  <div class="mark"></div><h2 class="title">Monthly Report Chart</h2><div class="logo">NRV</div>
  <svg style="left:0;top:0" width="270" height="150" viewBox="0 0 270 150">
    <polyline points="30,70 55,57 80,78 105,70 130,79 155,74" fill="none" stroke="#e3242b" stroke-width=".6"/>
    <g font-size="2.8" fill="#555" text-anchor="middle"><text x="34" y="72">60</text><text x="60" y="57">78</text><text x="85" y="80">49</text><text x="110" y="70">60</text><text x="135" y="81">49</text><text x="160" y="74">56</text></g>
    <g font-size="2.4" fill="#888" text-anchor="middle"><text x="30" y="118">JAN</text><text x="55" y="118">FEB</text><text x="80" y="118">MARC</text><text x="105" y="118">APR</text><text x="130" y="118">MAY</text><text x="155" y="118">JUN</text></g>
    <path d="M189 40l6 3.5v7l-6 3.5-6-3.5v-7zM189 85l6 3.5v7l-6 3.5-6-3.5v-7z" fill="#e3242b"/>
    <g font-size="3.4" fill="#fff" text-anchor="middle" font-weight="500"><text x="189" y="48">49</text><text x="189" y="93">56</text></g>
  </svg>
  <p style="left:183px;top:56px;font-size:5.6px;color:#444">May</p>
  <p class="tiny" style="left:183px;top:64px;width:65px">Lorem ipsum dolor sit amet, consectetuer adipiscing elit. Maecenas porttitor congue massa.</p>
  <p style="left:183px;top:100px;font-size:5.6px;color:#444">Jun</p>
  <p class="tiny" style="left:183px;top:108px;width:65px">Lorem ipsum dolor sit amet, consectetuer adipiscing elit. Maecenas porttitor congue massa.</p>
  <p class="url">www.<b>norvapaint</b>.com</p><p class="page">page 21</p><div class="band"></div>
</section>

<!-- 22 Three point strategy -->
<section class="slide" style="left:326px;top:857px">
  <div class="mark"></div><h2 class="title">Three Poin Strategy</h2><div class="logo">NRV</div>
  <svg style="left:0;top:0" width="270" height="150" viewBox="0 0 270 150">
    <path d="M41 73l38 36 38-53" fill="none" stroke="#e3242b" stroke-width="4.5" stroke-linejoin="round"/>
    <g fill="#e3242b" stroke="#fff" stroke-width="1.2"><circle cx="41" cy="73" r="12"/><circle cx="76" cy="109" r="12"/><circle cx="113" cy="56" r="12"/></g>
    <g fill="#fff" text-anchor="middle"><text x="41" y="74" font-size="6.5">1</text><text x="76" y="110" font-size="6.5">2</text><text x="113" y="57" font-size="6.5">3</text><text x="41" y="79" font-size="2.4">56%</text><text x="76" y="115" font-size="2.4">76%</text><text x="113" y="62" font-size="2.4">89%</text></g>
  </svg>
  <div class="dash" style="left:156px;top:42px"></div><p style="left:156px;top:43px;font-size:6px;color:#555">56%</p><p class="tiny" style="left:156px;top:52px;width:72px">Lorem ipsum dolor sit amet, consectetuer adipiscing elit. Maecenas porttitor congue massa.</p>
  <div class="dash" style="left:156px;top:67px"></div><p style="left:156px;top:68px;font-size:6px;color:#555">76%</p><p class="tiny" style="left:156px;top:77px;width:72px">Lorem ipsum dolor sit amet, consectetuer adipiscing elit. Maecenas porttitor congue massa.</p>
  <div class="dash" style="left:156px;top:92px"></div><p style="left:156px;top:93px;font-size:6px;color:#555">89%</p><p class="tiny" style="left:156px;top:102px;width:72px">Lorem ipsum dolor sit amet, consectetuer adipiscing elit. Maecenas porttitor congue massa.</p>
  <p class="url">www.<b>norvapaint</b>.com</p><p class="page">page 22</p><div class="band"></div>
</section>

<!-- 23 Timeline chart -->
<section class="slide" style="left:606px;top:857px">
  <div class="mark"></div><h2 class="title">Timeline Chart</h2><div class="logo">NRV</div>
  <svg style="left:0;top:0" width="270" height="150" viewBox="0 0 270 150">
    <line x1="20" y1="103" x2="250" y2="103" stroke="#bbb" stroke-width=".4" stroke-dasharray="1.5 1.5"/>
    <g stroke-width=".6"><path d="M56 60v43M172 60v43M211 60v43" stroke="#4b5468"/><path d="M95 41v62M133 41v62" stroke="#e3242b"/></g>
    <g stroke="#e4e5e9" stroke-width="1.5"><circle cx="56" cy="60" r="10" fill="#4b5468"/><circle cx="133" cy="60" r="10" fill="#4b5468"/><circle cx="211" cy="60" r="10" fill="#4b5468"/><circle cx="95" cy="41" r="10" fill="#e3242b"/><circle cx="172" cy="41" r="10" fill="#e3242b"/></g>
    <g stroke="#e3242b" stroke-width=".5"><circle cx="56" cy="103" r="2.5" fill="#4b5468"/><circle cx="95" cy="103" r="2.5" fill="#e3242b" stroke="#fff"/><circle cx="133" cy="103" r="2.5" fill="#4b5468"/><circle cx="172" cy="103" r="2.5" fill="#e3242b" stroke="#fff"/><circle cx="211" cy="103" r="2.5" fill="#4b5468"/></g>
    <g font-size="3.6" fill="#fff" text-anchor="middle" font-weight="500"><text x="56" y="61.3">2020</text><text x="95" y="42.3">2021</text><text x="133" y="61.3">2022</text><text x="172" y="42.3">2023</text><text x="211" y="61.3">2024</text></g>
  </svg>
  <p class="tiny c" style="left:38px;top:110px;width:36px">Lorem ipsum dolor Sit ametan jokoe.</p>
  <p class="tiny c" style="left:77px;top:110px;width:36px">Lorem ipsum dolor Sit ametan jokoe.</p>
  <p class="tiny c" style="left:115px;top:110px;width:36px">Lorem ipsum dolor Sit ametan jokoe.</p>
  <p class="tiny c" style="left:154px;top:110px;width:36px">Lorem ipsum dolor Sit ametan jokoe.</p>
  <p class="tiny c" style="left:193px;top:110px;width:36px">Lorem ipsum dolor Sit ametan jokoe.</p>
  <p class="url">www.<b>norvapaint</b>.com</p><p class="page">page 23</p><div class="band"></div>
</section>

<!-- 24 Thank you -->
<section class="slide dark" style="left:885px;top:857px;background:linear-gradient(135deg,#111112 45%,#4a1114 75%,#b3181f)">
  <h2 class="c" style="left:0;top:46px;width:270px;font-size:15px;font-weight:700;color:#fff">Thank You</h2>
  <div style="left:76px;top:68px;width:118px;height:.6px;background:var(--red)"></div>
  <p class="tiny c" style="left:70px;top:73px;width:130px;color:#ddd">Lorem ipsum dolor sit amet, consectetuer adipiscing elit. Maecen portion congue massa. Fusce posuere, magna sed pulvinar ultricies, purus lectus.</p>
  <svg style="left:108px;top:93px" width="54" height="10" viewBox="0 0 54 10" fill="none" stroke="#fff" stroke-width=".5"><circle cx="5" cy="5" r="4"/><circle cx="27" cy="5" r="4"/><circle cx="49" cy="5" r="4"/></svg>
</section>

</body>
</html>
```